Organization for CEO's Needs New Rebranding Concept

(Please note: we are NOT looking for a logo design, just a concept design to create the brand(colours,designs) around our existing logo)
Our organization Helmway Circles Greece (www.helmwaycirclesgreece.org) is in the process of rebranding in all aspects including our website, imagery, and slogan.
We are looking for a concept that will encapsulate this rebranding/change in the form of an image that can then be adapted almost everywhere (website, presentations, posters etc).
Our new slogan is “The house of collective wisdom, and future thinking. A seal of leadership and positive impact.” Ideally, we would like this new concept to express this slogan (“house” is used metaphorically, we do not want it literally in the image).
Ultimately, we want the concept to express the elements of an ecosystem/community of CEO’s and entrepreneurs who have a powerful voice on leadership and move together to co-create value for themselves, their organizations and society for the future. It would help for the image to not be too complicated for it to adapt to various formats, dimensions and situations.
You can view our website to understand our identity and attempt to create a new brand for our organization that is more modern.
Target Market(s)
Our audience are CEO's and entrepreneurs in an exclusive community
Look and feel

```html
<!DOCTYPE html>
<html lang="en">
<head>
<meta charset="utf-8">
<title>Helmway Circles – Brand Banner</title>
<link rel="stylesheet" href="https://fonts.googleapis.com/css2?family=Poppins:wght@200;300;500;600;800&display=swap">
<style>
  :root {
    --stage: #a5b1be;
    --navy-deep: #0c2340;
    --navy: #133a5e;
    --wave-mid: #2f6a92;
    --wave-light: #5c8eae;
    --photo-light: #c3cad1;
    --photo-mid: #98a3ad;
    --white: #ffffff;
  }
  html, body {
    margin: 0;
    padding: 0;
    width: 1200px;
    height: 1200px;
    overflow: hidden;
    background: var(--stage);
    font-family: "Poppins", sans-serif;
  }
  .banner {
    position: absolute;
    left: 68px;
    top: 423px;
    width: 1064px;
    height: 355px;
    overflow: hidden;
    box-shadow: 0 6px 14px rgba(20, 35, 55, 0.35);
  }
  .banner-photo {
    position: absolute;
    inset: 0;
    background:
      radial-gradient(circle at 76% 47%, #5a5f6e 0, #6d6f7c 18%, rgba(152,163,173,0) 30%),
      linear-gradient(120deg, var(--photo-light), var(--photo-mid));
  }
  .banner-shapes {
    position: absolute;
    inset: 0;
    width: 100%;
    height: 100%;
  }
  .brand {
    position: absolute;
    left: 63px;
    top: 34px;
    display: flex;
    align-items: center;
    gap: 12px;
    color: var(--white);
  }
  .brand-dot {
    width: 64px;
    height: 64px;
    border: 2px solid var(--white);
    border-radius: 50%;
    box-sizing: border-box;
  }
  .brand-name {
    font-weight: 600;
    font-size: 19px;
    line-height: 1.1;
    letter-spacing: 0.2px;
  }
  .headline {
    position: absolute;
    left: 49px;
    top: 150px;
    margin: 0;
    color: var(--white);
    font-weight: 300;
    line-height: 1.22;
  }
  .headline .line { display: block; white-space: nowrap; }
  .headline .light { font-size: 32px; font-weight: 300; }
  .headline .thin { font-size: 37px; font-weight: 200; }
  .headline .bold { font-size: 37px; font-weight: 800; }
  .headline .strong { font-size: 37px; font-weight: 600; }
  .tagline {
    position: absolute;
    left: 49px;
    top: 284px;
    margin: 0;
    color: var(--white);
    font-size: 18.5px;
    font-weight: 500;
    white-space: nowrap;
  }
</style>
</head>
<body>
  <section class="banner">
    <div class="banner-photo" role="img" aria-label="Overhead photo of a circle of business leaders joining hands in the middle on a grey stone floor"></div>
    <svg class="banner-shapes" viewBox="0 0 1064 355" preserveAspectRatio="none" aria-hidden="true">
      <defs>
        <linearGradient id="navyFill" x1="0" y1="0" x2="1" y2="1">
          <stop offset="0" stop-color="#143d61"/>
          <stop offset="1" stop-color="#0b2240"/>
        </linearGradient>
      </defs>
      <path d="M0 0 H550 C505 40 500 120 560 190 C620 260 640 310 615 355 H0 Z" fill="var(--wave-light)" opacity="0.55"/>
      <path d="M0 0 H500 C470 40 468 110 520 180 C575 250 595 310 575 355 H0 Z" fill="var(--wave-mid)"/>
      <path d="M0 0 H465 C450 50 470 130 520 200 C560 260 575 310 570 355 H0 Z" fill="url(#navyFill)"/>
      <path d="M0 0 H440 C430 60 455 140 505 210 C545 270 560 315 555 355 H0 Z" fill="url(#navyFill)"/>
    </svg>

    <div class="brand">
      <div class="brand-dot"></div>
      <div class="brand-name">Helmway Circles<br>International</div>
    </div>

    <h1 class="headline">
      <span class="line light">THE HOUSE OF</span>
      <span class="line bold">COLLECTIVE WISDOM,</span>
      <span class="line"><span class="thin">AND </span><span class="strong">FUTURE THINKING</span></span>
    </h1>
    <p class="tagline">A SEAL OF LEADERSHIP AND POSITIVE IMPACT</p>
  </section>
</body>
</html>
```